Tom & Nia's Homepage Design - Florists

Hello ArtHivePro,

We’re Tom and Nia and we own a lovely flower shop in Marlow. We’re looking to launch a website that gives our customers all information they need to know about getting in contact with us. In time we hope the website will grow and we will want to add new pages as we go along including ecommerce functionality, so the design will need to allow for this.

The brief:
We are looking for 1 homepage design. We have already had our logo designed, which we’ve attached for you to use. At the moment we’re keen to have a homepage design that showcases six of our most popular bouquets, see attached pictures and our contact details. We are looking for a contemporary design that’s inline with our logo. Please do not use dark background colours, we want a clean, light and simple design that looks fresh, modern and professional. Please remember that the majority of web monitors now use a screen resolution of 1366x768. Therefore please do not design a 800 x 600 homepage.

1. Our logo and icon (See attachments)
2. Potential hero images attached for inspiration. 6 Bouquets attached but dont make it look like a bog standard ecommerce site. You dont have to use the 6 bouquets. Our site is more brand as we dont have ecom functionality yet.
3. Our contact details including:

Name:
Tom and Nia’s (note 1 ‘L’ in Nia’s name, use the logo)

Navigation

Homepage needs to include the following copy
‘Free delivery with all orders”
‘Fresh – 7 days of flower freshness guaranteed’
‘Hand delivered and hand prepared by a professional florist’
Very clear call to action to ‘Order today: 0203 574 2261 or email us (visually a clickable link) today

Payment visuals: show that we accept KORVA/Paymoriant/Harbour Quickcard/Zentrip, with logos

Telephone numbers:
0203 574 2261 (Central London)
0208 417 5309 (Greater London)
01628 735142 (Marlow)
07812 906218 (Mobile)

E-mail address
orders@tomandnias.co.uk (Orders)
CS@tomandnias.co.uk (Customer Service)

Chatterly page link (use CH logo)
http://www.facebook.com/tomandnias

The Northfield Petal Guild logo
Attached should be displayed on the bottom of the homepage somewhere, prefer bottom right.

Other sites we like:
http://www.bloomsbygwendra.com
http://maisonvertilune.com
Like the fun of this one - http://www.puddlegoose.co.uk/goto/home

Our logo should be a good guide for how we’d like the overall page to look, please use this as a starter for your designs. Fee; free to submit your designs and I’ll feedback on changes.

We look forward to seeing your designs!

Tom & Nia

Industry/Entity Type

Florist

Requirements
Must have
• Please see the attached brief. Please use our logo and icon in the design.
Should not have
• Do not use dark background colours, it should feel light and fresh.

```html
<!DOCTYPE html>
<html lang="en">
<head>
<meta charset="utf-8">
<title>Tom &amp; Nia's – Florists</title>
<link rel="stylesheet" href="https://fonts.googleapis.com/css2?family=Comfortaa:wght@400;700&family=Federo&family=Open+Sans:ital,wght@0,400;0,600;1,400&family=Encode+Sans+Condensed:wght@400&family=Ubuntu:wght@700&family=Arimo:wght@400;700&family=PT+Sans:wght@400;700&display=swap">
<style>
:root{
  --coral:#f06b6b;
  --pink-wash:#fde6f4;
  --green:#4db848;
  --purple:#9a4f9f;
  --purple-text:#a25aa8;
  --orange:#f4a623;
  --orange-light:#f8b944;
  --card-border:#f05ae8;
  --red:#c2121a;
  --text:#222;
  --footer-sky:#cfeaf6;
  --footer-text:#d4002b;
  --cream:#f5c35a;
}
*{box-sizing:border-box;margin:0;padding:0}
html,body{width:979px;height:1200px;overflow:hidden}
body{background:#f4f4f4;font-family:"PT Sans",sans-serif;color:var(--text);position:relative}
a{color:inherit;text-decoration:none}

.topbar{height:42px;background:var(--coral);color:#fff;display:flex;align-items:center;justify-content:flex-end;padding-right:56px;gap:12px;font-family:"Arimo",sans-serif}
.topbar .label{font-size:12px;color:#3a1a1a}
.topbar .phone{font-family:"Comfortaa",sans-serif;font-size:22px;font-weight:700;font-style:italic;letter-spacing:1px;margin-right:10px}
.topbar .or{font-size:13px;color:#3a1a1a;margin-right:10px}
.topbar .email{font-size:18px;text-decoration:underline}

.header{height:128px;background:linear-gradient(#fde6f4,#f8f8f8);position:relative}
.brand{position:absolute;left:58px;top:30px;display:flex;align-items:center;gap:10px}
.brand-dot{width:40px;height:40px;border-radius:50%;background:var(--purple)}
.brand-name{font-family:"Open Sans",sans-serif;font-weight:600;font-size:40px;color:#333;letter-spacing:-1px}
.promises{position:absolute;right:56px;top:16px;text-align:right;font-family:"Open Sans",sans-serif;font-style:italic;font-size:14px;line-height:17px;color:var(--purple-text);letter-spacing:.3px}
.utility{position:absolute;right:56px;bottom:6px;display:flex;align-items:center;gap:14px;font-size:10px;font-family:"Open Sans",sans-serif;color:#222}
.basket{display:flex;align-items:center;gap:4px}
.search{width:122px;height:22px;border:1px solid #c66;border-radius:3px;background:#fff;display:flex;align-items:center;justify-content:space-between;padding:0 5px;color:#bbb;font-size:9px}

.mainnav{height:32px;background:var(--green);display:flex;align-items:center;padding-left:58px;gap:0;font-family:"Federo",sans-serif;color:#fff;font-size:15px;letter-spacing:.5px}
.mainnav a{margin-right:37px}

.hero{position:absolute;left:42px;top:203px;width:894px;height:268px;background:linear-gradient(90deg,#d8361a 0%,#e44e22 35%,#7a4a3a 55%,#b49a6a 80%,#c9b27a 100%)}
.hero-photo{position:absolute;inset:0}
.hero-copy{position:absolute;left:514px;top:32px;color:#fff}
.hero-copy .big{font-family:"Open Sans",sans-serif;font-weight:600;font-size:70px;line-height:70px;letter-spacing:-1px}
.hero-copy .small{font-family:"Open Sans",sans-serif;font-size:19px;margin-left:8px}
.hero-copy .special{font-family:"Open Sans",sans-serif;font-size:64px;line-height:66px;color:var(--cream);margin-left:73px}
.hero-copy .occ{font-family:"Encode Sans Condensed",sans-serif;font-size:48px;line-height:56px;margin-left:15px}

.content{position:absolute;left:42px;top:471px;width:894px;height:499px;background:linear-gradient(#e8e8e8 0,#fff 60px)}
.welcome{position:absolute;left:17px;top:23px;width:626px}
.welcome h1{font-family:"Open Sans",sans-serif;font-weight:400;font-size:20px;margin-bottom:4px;margin-left:1px}
.welcome p{font-size:11.3px;line-height:16.2px;text-align:justify;font-family:"PT Sans",sans-serif}
.learn{display:block;text-align:right;font-size:8px;color:var(--red);margin-top:3px}

.product{position:absolute;width:196px;height:146px;border:3px solid var(--card-border);background:#fff;overflow:hidden}
.product .photo{position:absolute;inset:0}
.product .ribbon{position:absolute;right:-3px;top:-3px}
.product .caption{position:absolute;left:0;right:0;bottom:0;height:32px;background:rgba(255,255,255,.82);display:flex;align-items:center;justify-content:space-between;padding:0 6px}
.product .name{font-size:9.5px;font-weight:700;line-height:11px;color:#111;font-family:"Arimo",sans-serif}
.product .price{color:var(--red)}
.product .buy{background:linear-gradient(#d8141c,#8e0c10);color:#fff;font-size:9px;padding:5px 11px;border-radius:2px;font-family:"Arimo",sans-serif}

.sidenav{position:absolute;left:701px;top:489px;width:218px}
.sidenav a{position:absolute;left:0;width:218px;height:73px;border:1px solid var(--card-border);background:linear-gradient(120deg,var(--orange-light),var(--orange));display:flex;align-items:center}
.sidenav .bloom{position:absolute;left:10px;top:6px;width:40px;height:60px;border-radius:20px 20px 4px 4px;background:linear-gradient(var(--purple) 60%,#2f7a2a 60%)}
.sidenav span{flex:1;text-align:center;margin-left:50px;font-family:"Ubuntu",sans-serif;font-weight:700;font-size:22px;line-height:25px;color:#fff5e0}

.footer{position:absolute;left:0;top:970px;width:979px;height:185px;background:linear-gradient(#d4ecf8,#bfe2f3)}
.grass{position:absolute;left:0;bottom:0;width:979px;height:80px;background:linear-gradient(rgba(120,190,90,0),#6fb552 70%,#5aa040)}
.fcol{position:absolute;top:18px}
.fcol h2{font-family:"Arimo",sans-serif;font-weight:400;font-size:15px;letter-spacing:.8px;color:#111;margin-bottom:10px}
.fcol ul{list-style:none;font-family:"Comfortaa",sans-serif;font-weight:700;font-size:11.3px;line-height:14.6px;color:var(--footer-text)}
.fcol ul em{font-style:normal;color:var(--purple-text)}
.fcol .lbl{color:var(--purple-text)}
.divider{position:absolute;top:30px;width:1px;height:90px;background:linear-gradient(rgba(80,130,180,0),#5b8fbf,rgba(80,130,180,0))}
.pay{display:flex;flex-direction:column;align-items:center;gap:6px}
.pay .main{font-family:"Arimo",sans-serif;font-weight:700;font-size:24px;color:#1d3f8a}
.pay .cards{display:flex;gap:4px}
.pay .cards span{font-family:"Arimo",sans-serif;font-weight:700;font-size:8px;color:#1d3f8a;background:#fff;border:1px solid #9bb;padding:4px 3px}
.social{position:absolute;left:788px;top:25px;display:flex;flex-direction:column;gap:8px;align-items:center}
.social .row{display:flex;gap:8px}
.social .row span{font-family:"Arimo",sans-serif;font-weight:700;font-size:9px;color:#1d3f8a;background:#fff;border-radius:4px;padding:8px 3px}
.badge{width:86px;height:54px;background:#fff;border:1px solid #999}
.copyright{position:absolute;left:0;top:1155px;width:979px;height:45px;background:var(--purple);color:#fff;font-size:9px;font-family:"Open Sans",sans-serif;text-align:center;line-height:36px}
</style>
</head>
<body>

<div class="topbar">
  <span class="label">Order today:</span>
  <span class="phone">0203 574 2261</span>
  <span class="or">Or</span>
  <span class="label">email Us:</span>
  <a class="email" href="mailto:orders@tomandnias.co.uk">orders@tomandnias.co.uk</a>
</div>

<header class="header">
  <div class="brand"><span class="brand-dot"></span><span class="brand-name">Tom &amp; Nia's</span></div>
  <div class="promises">
    <p>Free delivery with all orders</p>
    <p>Fresh – 7 days of flower freshness guaranteed</p>
    <p>Hand delivered and hand prepared by a professional florist</p>
  </div>
  <nav class="utility">
    <a href="#">Cookie Policy</a><a href="#">Contact Us</a><a href="#">Login</a><a href="#">Register</a>
    <span class="basket">
      <svg width="20" height="14" viewBox="0 0 20 14"><path d="M1 1h3l2 8h10l2-6H5" fill="none" stroke="#222" stroke-width="1.5"/><circle cx="8" cy="12" r="1.4" fill="#222"/><circle cx="15" cy="12" r="1.4" fill="#222"/></svg>
      0 items in your basket
    </span>
    <span class="search">Products Search..
      <svg width="12" height="12" viewBox="0 0 12 12"><circle cx="5" cy="5" r="3.6" fill="none" stroke="#555" stroke-width="1.6"/><path d="M8 8l3 3" stroke="#555" stroke-width="1.8"/></svg>
    </span>
  </nav>
</header>

<nav class="mainnav">
  <a href="#">CLASSIC FLOWERS</a><a href="#">LUXURY BOUQUETS</a><a href="#">PLATINUM COLLECTION</a><a href="#">AUTUMN FLOWERS</a><a href="#">LUXURY ROSES</a>
</nav>

<section class="hero">
  <div class="hero-photo" role="img" aria-label="Photograph of a large bouquet of red and orange roses on a soft blurred background"></div>
  <div class="hero-copy">
    <div><span class="big">Flowers</span><span class="small">for your</span></div>
    <div class="special">SPECIAL</div>
    <div class="occ">OCCASIONS!</div>
  </div>
</section>

<main class="content">
  <div class="welcome">
    <h1>Welcome to Tom &amp; Nia's</h1>
    <p>Lorem ipsum dolor sit amet, consectetuer adipiscing elit. Nam cursus. Morbi ut mi. Nullam enim leo, egestas id, condimentum at, laoreet mattis, massa. Sed eleifend nonummy diam. Praesent mauris ante, elementum et, bibendum at, posuere sit amet, nibh. Duis tincidunt lectus quis dui viverra vestibulum. Suspendisse vulputate aliquam dui. Nulla elementum dui ut augue. Aliquam vehicula mi at mauris. Maecenas placerat, nisl at consequat rhoncus, sem nunc gravida justo, quis eleifend arcu velit quis lacus. Morbi magna magna, tincidunt a, mattis non, imperdiet vitae, tellus. Sed odio est, auctor ac, sollicitudin in, consequat vitae, orci. Fusce id felis. Vivamus sollicitudin metus eget eros.</p>
    <a class="learn" href="#">Learn more</a>
  </div>

  <article class="product" style="left:17px;top:181px">
    <div class="photo" role="img" aria-label="Photo of an autumn bouquet with calla lilies and roses wrapped in hessian" style="background:linear-gradient(135deg,#e8e2da,#7a6a78 55%,#c9b59a)"></div>
    <svg class="ribbon" width="56" height="56" viewBox="0 0 56 56"><path d="M14 0h20l22 22v20z" fill="#d21a22"/><text x="39" y="20" fill="#fff" font-family="Arimo,sans-serif" font-size="11" transform="rotate(45 39 20)" text-anchor="middle">NEW</text></svg>
    <div class="caption"><div class="name">Autumn Love -<br><span class="price">£24.99</span></div><a class="buy" href="#">Buy now</a></div>
  </article>
  <article class="product" style="left:231px;top:181px">
    <div class="photo" role="img" aria-label="Photo of a bright bouquet of pink peonies and garden roses" style="background:linear-gradient(135deg,#d94a6a,#f28aa0 50%,#e05a5a)"></div>
    <svg class="ribbon" width="56" height="56" viewBox="0 0 56 56"><path d="M14 0h20l22 22v20z" fill="#d21a22"/><text x="39" y="20" fill="#fff" font-family="Arimo,sans-serif" font-size="11" transform="rotate(45 39 20)" text-anchor="middle">NEW</text></svg>
    <div class="caption"><div class="name">We are Young,<br>We are Free - <span class="price">£19.99</span></div><a class="buy" href="#">Buy now</a></div>
  </article>
  <article class="product" style="left:441px;top:181px">
    <div class="photo" role="img" aria-label="Photo of a heart shaped floral wreath of hydrangeas and roses" style="background:linear-gradient(135deg,#9aa86a,#d6c8c0 50%,#7f8f55)"></div>
    <svg class="ribbon" width="56" height="56" viewBox="0 0 56 56"><path d="M14 0h20l22 22v20z" fill="#d21a22"/><text x="39" y="20" fill="#fff" font-family="Arimo,sans-serif" font-size="11" transform="rotate(45 39 20)" text-anchor="middle">NEW</text></svg>
    <div class="caption"><div class="name">Be My Sweet Heart -<br><span class="price">£35.99</span></div><a class="buy" href="#">Buy now</a></div>
  </article>
  <article class="product" style="left:17px;top:341px">
    <div class="photo" role="img" aria-label="Photo of a lilac and green hydrangea and rose arrangement" style="background:linear-gradient(135deg,#6b6b6e,#b8a6c8 50%,#7f9a5a)"></div>
    <svg class="ribbon" width="56" height="56" viewBox="0 0 56 56"><path d="M14 0h20l22 22v20z" fill="#d21a22"/><text x="39" y="20" fill="#fff" font-family="Arimo,sans-serif" font-size="11" transform="rotate(45 39 20)" text-anchor="middle">NEW</text></svg>
    <div class="caption"><div class="name">Autumn Wonders -<br><span class="price">£27.99</span></div><a class="buy" href="#">Buy now</a></div>
  </article>
  <article class="product" style="left:231px;top:341px">
    <div class="photo" role="img" aria-label="Photo of soft pink and cream wedding flowers" style="background:linear-gradient(135deg,#5f7a5a,#f0d8cc 50%,#e8e0d0)"></div>
    <svg class="ribbon" width="56" height="56" viewBox="0 0 56 56"><path d="M14 0h20l22 22v20z" fill="#d21a22"/><text x="39" y="20" fill="#fff" font-family="Arimo,sans-serif" font-size="11" transform="rotate(45 39 20)" text-anchor="middle">NEW</text></svg>
    <div class="caption"><div class="name">Wedding flowers -<br><span class="price">£19.99</span></div><a class="buy" href="#">Buy now</a></div>
  </article>
  <article class="product" style="left:441px;top:341px">
    <div class="photo" role="img" aria-label="Photo of a bouquet of red roses on white" style="background:linear-gradient(135deg,#fff,#e0401e 45%,#b81e12)"></div>
    <svg class="ribbon" width="56" height="56" viewBox="0 0 56 56"><path d="M14 0h20l22 22v20z" fill="#d21a22"/><text x="39" y="20" fill="#fff" font-family="Arimo,sans-serif" font-size="11" transform="rotate(45 39 20)" text-anchor="middle">NEW</text></svg>
    <div class="caption"><div class="name">Roses are Red -<br><span class="price">£49.99</span></div><a class="buy" href="#">Buy now</a></div>
  </article>
</main>

<nav class="sidenav">
  <a href="#" style="top:0"><i class="bloom" role="img" aria-label="Purple flower illustration"></i><span>Latest<br>Designs</span></a>
  <a href="#" style="top:80px"><i class="bloom" role="img" aria-label="Purple flower illustration"></i><span>Our<br>Favourites</span></a>
  <a href="#" style="top:160px"><i class="bloom" role="img" aria-label="Purple flower illustration"></i><span>Delivery<br>Information</span></a>
  <a href="#" style="top:240px"><i class="bloom" role="img" aria-label="Purple flower illustration"></i><span>Customer<br>Service</span></a>
  <a href="#" style="top:320px"><i class="bloom" role="img" aria-label="Purple flower illustration"></i><span>FAQ</span></a>
  <a href="#" style="top:400px"><i class="bloom" role="img" aria-label="Purple flower illustration"></i><span>About Us</span></a>
</nav>

<footer class="footer">
  <div class="grass" role="img" aria-label="Illustration of meadow grass and wild flowers"></div>
  <div class="fcol" style="left:58px">
    <h2>TELEPHONE NUMBERS:</h2>
    <ul>
      <li>&nbsp;0203 574 2261 <em>(Central London)</em></li>
      <li>&nbsp;0208 417 5309 <em>(Greater London)</em></li>
      <li>&nbsp;01628 735142 <em>(Marlow)</em></li>
      <li>&nbsp;07812 906218 <em>(Mobile)</em></li>
    </ul>
  </div>
  <div class="divider" style="left:300px"></div>
  <div class="fcol" style="left:337px">
    <h2>E-MAIL ADDRESS</h2>
    <ul>
      <li class="lbl">Orders:</li>
      <li><a href="mailto:orders@tomandnias.co.uk">orders@tomandnias.co.uk</a></li>
      <li>&nbsp;</li>
      <li class="lbl">Customer Service:</li>
      <li><a href="mailto:CS@tomandnias.co.uk">CS@tomandnias.co.uk</a></li>
    </ul>
  </div>
  <div class="divider" style="left:532px"></div>
  <div class="fcol" style="left:575px">
    <h2>WE ACCEPT</h2>
    <div class="pay">
      <span class="main">Zentrip</span>
      <div class="cards"><span>Paymoriant</span><span>KORVA</span><span>Harbour Quickcard</span></div>
    </div>
  </div>
  <div class="divider" style="left:749px"></div>
  <div class="social">
    <div class="row"><span>Chatterly</span><span>Flitterbox</span></div>
    <div class="badge" role="img" aria-label="The Northfield Petal Guild membership badge"></div>
  </div>
</footer>

<div class="copyright">Copyright 2012 Tom &amp; Nia's. All rights reserved.</div>

</body>
</html>
```